Business Card for: Northbrook Financial Advisory Services Inc.

provide strategic financial advisory services to companies in the areas of corporate finance, mergers and acquisitions, executive coaching and strategic planning

Target Market(s)

Companies, banks, accountants, lawyers

Industry/Entity Type

High end business consulting in corporate finance, mergers and acquisitions, consulting

Contact Information for Business Card

Name of company, Name: xxxxxx xxxxxx , CEO, - phone number: 1-xxx-xxx-xxxx, - email address,

Requirements
Must have
• Must be professional and simple.
Nice to have
• simple, straight graphics, must give the impression that we are trustworthy, professional, competent
Should not have
• loud colors, loud design features

```html
<!DOCTYPE html>
<html lang="en">
<head>
<meta charset="utf-8">
<title>Northbrook Financial Advisory Services Inc. – Business Card</title>
<link rel="stylesheet" href="https://fonts.googleapis.com/css2?family=Jost:wght@400;500;600&display=swap">
<style>
  :root {
    --backdrop: #363636;
    --navy: #001738;
    --steel-blue: #3f6fa9;
    --paper: #ffffff;
  }
  html, body {
    margin: 0;
    padding: 0;
    width: 1200px;
    height: 1200px;
    overflow: hidden;
    background: var(--backdrop);
  }
  .canvas {
    position: relative;
    width: 1200px;
    height: 1200px;
  }
  .card {
    position: absolute;
    left: 216px;
    width: 768px;
    height: 438px;
    box-shadow: 0 6px 18px rgba(0, 0, 0, 0.35);
    background: var(--paper);
  }
  .card--front { top: 130px; }
  .card--back { top: 631px; }
  .card svg {
    display: block;
    width: 100%;
    height: 100%;
  }
  .fill-navy { fill: var(--navy); }
  .fill-blue { fill: var(--steel-blue); }
  .type {
    font-family: "Jost", "Futura", sans-serif;
  }
  .company-name { font-weight: 500; letter-spacing: 1px; }
  .person-name { font-weight: 600; letter-spacing: 16px; fill: var(--navy); }
  .person-role { font-weight: 500; letter-spacing: 8px; fill: var(--steel-blue); }
  .contact-value { font-weight: 400; letter-spacing: 5px; fill: var(--navy); }
  .icon { fill: none; stroke: var(--navy); stroke-width: 4; }
</style>
</head>
<body>
<main class="canvas">

  <!-- Front of card: brand panel and contact details -->
  <section class="card card--front" aria-label="Business card front">
    <svg viewBox="0 0 1237 706" xmlns="http://www.w3.org/2000/svg">
      <polygon class="fill-blue" points="413,48 467,48 569,354 467,658 413,658 515,354"/>
      <polygon class="fill-navy" points="0,0 396,0 515,354 396,706 0,706"/>
      <polygon class="fill-blue" points="1237,321 1237,706 1107,706"/>
      <polygon class="fill-navy" points="1237,449 1237,706 1151,706"/>

      <g class="type company-name" fill="#ffffff" font-size="34" text-anchor="middle">
        <text x="231" y="340">Northbrook Financial</text>
        <text x="231" y="382">Advisory Services Inc.</text>
      </g>

      <g class="type identity">
        <text class="person-name" x="890" y="212" font-size="68" text-anchor="middle">NAME HERE</text>
        <text class="person-role" x="888" y="265" font-size="38" text-anchor="middle">CEO</text>
        <line x1="652" y1="313" x2="1121" y2="313" stroke="var(--steel-blue)" stroke-width="2.5"/>
      </g>

      <g class="contact-row contact-row--phone">
        <rect class="icon" x="708" y="391" width="34" height="62" rx="3"/>
        <line class="icon" x1="718" y1="395" x2="732" y2="395" stroke-width="3"/>
        <text class="type contact-value" x="787" y="434" font-size="34">XXXXXXXXXXX</text>
      </g>
      <g class="contact-row contact-row--email">
        <rect class="icon" x="704" y="488" width="51" height="31"/>
        <polyline class="icon" points="704,488 729.5,508 755,488" stroke-width="3"/>
        <line class="icon" x1="704" y1="519" x2="722" y2="503" stroke-width="3"/>
        <line class="icon" x1="755" y1="519" x2="737" y2="503" stroke-width="3"/>
        <text class="type contact-value" x="790" y="516" font-size="34">XXXXXXXXXXX</text>
      </g>
    </svg>
  </section>

  <!-- Back of card: centred company name -->
  <section class="card card--back" aria-label="Business card back">
    <svg viewBox="0 0 1237 706" xmlns="http://www.w3.org/2000/svg">
      <polygon class="fill-blue" points="87,0 131,0 0,386 0,256"/>
      <polygon class="fill-navy" points="0,0 87,0 0,256"/>
      <polygon class="fill-blue" points="1237,321 1237,706 1107,706"/>
      <polygon class="fill-navy" points="1237,449 1237,706 1151,706"/>

      <g class="type company-name" fill="var(--navy)" font-size="56" text-anchor="middle">
        <text x="621" y="340">Northbrook Financial</text>
        <text x="621" y="408">Advisory Services Inc.</text>
      </g>
    </svg>
  </section>

</main>
</body>
</html>
```